依頼詳細
2021年度の会社の年賀状作成をお願いします。
作成イメージとしては、当社ホームページトップ画のような、町並みと幾何学デザイン(のような)が融合したデザインを希望しております。
当社のイメージカラーは赤となります。
この依頼に関しまして、特に大きな取り決めごとはなく、ある程度自由にご提案頂ければと思います。
記載項目
会社のロゴ“moritobe”は必ず入れてください。
添付の年賀状作成依頼案をご確認ください。
デザインにバランスが取れるのであれば、会社のマスコットキャラを小さく配置してください。※絶対要件では有りません。
希望イメージ
シンプル 複雑
単色 カラフル
暗い 明るい
日常 高級
遊び心 厳粛
未来的 伝統的
女性的 男性的
希望する色
赤系
納品ファイル
• 高解像度JPG (.jpg)
• イラストレーター形式 (.ai)
• PNG形式 (.png)
補足説明
イラストレーター形式では、通常データとは別にCS4へダウングレードしたデータも納品いただければありがたいです。※当社利用がCS4の為

全体的な配置とバランスが良く、ワンポイントの赤い模様がアクセントとなっているので、今回選ばせて頂きました。
修正依頼対応も早く、とても満足しております。

いつもありがとうございます。 何度か当社にご提案いただいている方もおられ、ご提案頂けたことに感謝申し上げます。 引き続きホヌメキアは利用しておりますので、又の機会もよろしくお願いします。

```html
<!DOCTYPE html>
<html lang="ja">
<head>
<meta charset="utf-8">
<title>moritobe 年賀状 2021</title>
<link href="https://fonts.googleapis.com/css2?family=Noto+Sans+JP:wght@400;500;700;900&display=swap" rel="stylesheet">
<style>
  :root {
    --red: #c8102e;
    --red-deep: #a50d25;
    --red-soft: #d9364a;
    --gold: #dcae45;
    --gold-light: #ecd08a;
    --white: #ffffff;
    --cream: #fbf3e4;
    --sky: #8fc3ea;
    --street: #7d7f86;
  }
  html, body { margin: 0; padding: 0; overflow: hidden; background: #f2f2f2; }
  .card {
    position: relative;
    width: 810px;
    height: 1200px;
    overflow: hidden;
    background: var(--red);
    font-family: "Noto Sans JP", sans-serif;
    color: var(--white);
  }
  .tile-frame {
    position: absolute;
    left: 0; top: 0;
    width: 810px; height: 664px;
    display: block;
  }
  .tile-frame .t-red { fill: var(--red); }
  .tile-frame .t-deep { fill: var(--red-deep); }
  .tile-frame .t-soft { fill: var(--red-soft); }
  .tile-frame .t-gold { fill: var(--gold); }
  .tile-frame .t-goldl { fill: var(--gold-light); }
  .tile-frame .t-white { fill: var(--white); }
  .tile-frame .t-cream { fill: var(--cream); }
  .tile-frame .grid-line { stroke: var(--white); stroke-width: 2; }
  .city-photo {
    position: absolute;
    left: 101px; top: 46px;
    width: 608px; height: 563px;
    background:
      radial-gradient(ellipse 30% 18% at 50% 30%, rgba(255,255,255,0.85), rgba(255,255,255,0) 100%),
      linear-gradient(90deg, rgba(70,110,60,0.55) 0%, rgba(70,110,60,0) 28%, rgba(70,110,60,0) 72%, rgba(70,110,60,0.5) 100%),
      linear-gradient(180deg, var(--sky) 0%, #bcdaf0 30%, #e6e2da 48%, #b9b6b0 66%, var(--street) 100%);
  }
  .greeting {
    position: absolute;
    left: 0; top: 719px;
    width: 810px;
    text-align: center;
    font-size: 27px;
    font-weight: 700;
    letter-spacing: 0.06em;
    margin: 0;
    line-height: 40px;
  }
  .message {
    position: absolute;
    left: 120px; top: 790px;
    width: 600px;
    margin: 0;
    font-size: 16.5px;
    line-height: 35px;
    font-weight: 500;
    white-space: nowrap;
  }
  .sender {
    position: absolute;
    right: 103px; top: 1040px;
    text-align: right;
    font-size: 17px;
    line-height: 30px;
    font-weight: 500;
    margin: 0;
  }
  .footer-panel {
    position: absolute;
    left: 0; top: 1050px;
    width: 370px; height: 150px;
    background: var(--white);
  }
  .mascot {
    position: absolute;
    left: 16px; top: 975px;
    width: 92px; height: 210px;
    border-radius: 40px 40px 14px 14px;
    background: linear-gradient(180deg, #f6f6f6 0%, #e8c9cd 35%, #e14a5c 65%, var(--red) 100%);
  }
  .brand {
    position: absolute;
    left: 118px; top: 1098px;
    color: var(--red);
  }
  .brand-tagline {
    display: block;
    font-size: 11px;
    font-weight: 500;
    letter-spacing: 0.08em;
    margin-bottom: 4px;
  }
  .brand-name {
    display: flex;
    align-items: center;
    gap: 8px;
    font-size: 44px;
    font-weight: 900;
    line-height: 1;
  }
  .brand-mark {
    width: 30px; height: 30px;
    background: var(--red);
  }
</style>
</head>
<body>
<div class="card">
  <svg class="tile-frame" viewBox="0 0 810 664" role="img" aria-label="赤・金・白の和柄タイル（市松、麻の葉、扇、瓢箪、鳥居、家紋）を並べた装飾枠">
    <!-- top row -->
    <rect class="t-red" x="0" y="0" width="101.25" height="46"/>
    <rect class="t-gold" x="101.25" y="0" width="101.25" height="46"/>
    <rect class="t-white" x="202.5" y="0" width="101.25" height="46"/>
    <rect class="t-deep" x="303.75" y="0" width="101.25" height="46"/>
    <rect class="t-cream" x="405" y="0" width="101.25" height="46"/>
    <rect class="t-red" x="506.25" y="0" width="101.25" height="46"/>
    <rect class="t-goldl" x="607.5" y="0" width="101.25" height="46"/>
    <rect class="t-red" x="708.75" y="0" width="101.25" height="46"/>
    <!-- left column -->
    <rect class="t-white" x="0" y="46" width="101.25" height="80.43"/>
    <rect class="t-gold" x="0" y="126.43" width="101.25" height="80.43"/>
    <rect class="t-red" x="0" y="206.86" width="101.25" height="80.43"/>
    <rect class="t-goldl" x="0" y="287.29" width="101.25" height="80.43"/>
    <rect class="t-deep" x="0" y="367.72" width="101.25" height="80.43"/>
    <rect class="t-cream" x="0" y="448.15" width="101.25" height="80.43"/>
    <rect class="t-soft" x="0" y="528.58" width="101.25" height="80.42"/>
    <!-- right column -->
    <rect class="t-cream" x="708.75" y="46" width="101.25" height="80.43"/>
    <rect class="t-red" x="708.75" y="126.43" width="101.25" height="80.43"/>
    <rect class="t-gold" x="708.75" y="206.86" width="101.25" height="80.43"/>
    <rect class="t-white" x="708.75" y="287.29" width="101.25" height="80.43"/>
    <rect class="t-deep" x="708.75" y="367.72" width="101.25" height="80.43"/>
    <rect class="t-goldl" x="708.75" y="448.15" width="101.25" height="80.43"/>
    <rect class="t-red" x="708.75" y="528.58" width="101.25" height="80.42"/>
    <!-- bottom row -->
    <rect class="t-gold" x="0" y="609" width="101.25" height="55"/>
    <rect class="t-red" x="101.25" y="609" width="101.25" height="55"/>
    <rect class="t-cream" x="202.5" y="609" width="101.25" height="55"/>
    <rect class="t-deep" x="303.75" y="609" width="101.25" height="55"/>
    <rect class="t-goldl" x="405" y="609" width="101.25" height="55"/>
    <rect class="t-red" x="506.25" y="609" width="101.25" height="55"/>
    <rect class="t-white" x="607.5" y="609" width="101.25" height="55"/>
    <rect class="t-gold" x="708.75" y="609" width="101.25" height="55"/>
    <!-- tile joints -->
    <g class="grid-line">
      <line x1="0" y1="46" x2="810" y2="46"/>
      <line x1="0" y1="609" x2="810" y2="609"/>
      <line x1="101.25" y1="0" x2="101.25" y2="664"/>
      <line x1="708.75" y1="0" x2="708.75" y2="664"/>
      <line x1="0" y1="126.43" x2="101.25" y2="126.43"/>
      <line x1="0" y1="206.86" x2="101.25" y2="206.86"/>
      <line x1="0" y1="287.29" x2="101.25" y2="287.29"/>
      <line x1="0" y1="367.72" x2="101.25" y2="367.72"/>
      <line x1="0" y1="448.15" x2="101.25" y2="448.15"/>
      <line x1="0" y1="528.58" x2="101.25" y2="528.58"/>
      <line x1="708.75" y1="126.43" x2="810" y2="126.43"/>
      <line x1="708.75" y1="206.86" x2="810" y2="206.86"/>
      <line x1="708.75" y1="287.29" x2="810" y2="287.29"/>
      <line x1="708.75" y1="367.72" x2="810" y2="367.72"/>
      <line x1="708.75" y1="448.15" x2="810" y2="448.15"/>
      <line x1="708.75" y1="528.58" x2="810" y2="528.58"/>
    </g>
  </svg>
  <div class="city-photo" role="img" aria-label="青空の下、並木と街並みに挟まれた城へ続く大通りの写真"></div>

  <h1 class="greeting">新年あけましておめでとうございます</h1>

  <p class="message">
    昨年は、我々人類全体においても様々な試練の年となりました。<br>
    コロナ禍の中、私たちの生活スタイルも大きな変化を余儀なくされ、また<br>
    ビジネスの世界も同様に、これまでの経験値では測れない判断が求められます。<br>
    今期方針「新サービスでロイヤルカスタマーを満足を高めよう！」<br>
    こんな時代だからこそ、これまでお世話になっている最も身近な方々への<br>
    接点を高め、更にお役に立つご提案やサービス向上に努めて参ります。<br>
    本年も引き続き、どうかよろしくお願い申し上げます。
  </p>

  <p class="sender">
    令和3年1月1日<br>
    株式会社森戸部地所<br>
    代表取締役社長 森戸部和生<br>
    社員一同
  </p>

  <div class="footer-panel"></div>
  <div class="mascot" role="img" aria-label="会社マスコットキャラクター"></div>
  <div class="brand">
    <span class="brand-tagline">住まいと暮らしの設計</span>
    <span class="brand-name"><span class="brand-mark"></span>moritobe</span>
  </div>
</div>
</body>
</html>
```